LOS PINOS DE ARENA - EXCLUSIVE AND LUXURY REAL ESTATE PROJECT

Se trata del diseño de un mono poste grande (4 m x 2 m) o (8m x 3m) anunciando la construcción de 30 villas de lujo en un terreno en primera línea de playa en el sur de España (Cádiz).

La idea es crear expectación y transmitir lujo y exclusividad.

Target Market(s)

Clientes de alto poder adquisitivo que quieran adquirir su segunda vivienda en un entorno privilegiado a escasos pasos de una de las playas más bonitas de Cádiz.

Industry/Entity Type

REAL ESTATE

Colors

Designer to choose colors to be used in the design.

Requirements
Must have
• LOS PINOS DE ARENA as the name of the development
Nice to have
• Crear expectación con ideas del tipo: “Coming soon” o “No te lo puedes perder”

```html
<!DOCTYPE html>
<html lang="es">
<head>
<meta charset="utf-8">
<title>Los Pinos de Arena – Coming Soon</title>
<link rel="stylesheet" href="https://fonts.googleapis.com/css2?family=Lexend:wght@600&family=Raleway:wght@200&display=swap">
<style>
  :root {
    --page-bg: #747474;
    --sign-white: #ffffff;
    --brand-blue: #3a60ab;
    --sky-top: #3b62ad;
    --sky-low: #5f86c6;
    --stone: #d8cdb0;
    --terrace: #e4e1da;
    --ink: #000000;
  }
  * { margin: 0; padding: 0; box-sizing: border-box; }
  html, body {
    width: 864px;
    height: 1200px;
    overflow: hidden;
    background: var(--page-bg);
  }
  .billboard {
    position: absolute;
    left: 32px;
    top: 400px;
    width: 800px;
    height: 400px;
    background: var(--sign-white);
  }
  .hero-panel {
    position: absolute;
    left: 23px;
    top: 22px;
    width: 419px;
    height: 358px;
    background: linear-gradient(180deg, var(--sky-top) 0%, var(--sky-low) 48%, #e9eaec 58%, var(--stone) 72%, var(--terrace) 100%);
  }
  .hero-panel__tagline {
    position: absolute;
    top: 14px;
    left: 0;
    width: 100%;
    text-align: center;
    font-family: "Raleway", sans-serif;
    font-weight: 200;
    font-size: 41px;
    letter-spacing: 1px;
    color: var(--sign-white);
    white-space: nowrap;
  }
  .project-name {
    position: absolute;
    left: 452px;
    top: 62px;
    font-family: "Lexend", sans-serif;
    font-weight: 600;
    font-size: 86px;
    line-height: 78px;
    letter-spacing: -3px;
  }
  .project-name__line { display: block; }
  .project-name__line--blue { color: var(--brand-blue); }
  .project-name__line--dark { color: var(--ink); }
  .side-strip {
    position: absolute;
    left: 756px;
    top: 22px;
    width: 22px;
    height: 350px;
    background: linear-gradient(180deg, var(--brand-blue) 0%, var(--sky-low) 40%, var(--stone) 50%, #e6dfcc 100%);
  }
</style>
</head>
<body>
  <div class="billboard">
    <div class="hero-panel" role="img" aria-label="Render of a modern white villa with terrace, pool and stone wall under a blue sky">
      <p class="hero-panel__tagline">COMING SOON</p>
    </div>
    <h1 class="project-name">
      <span class="project-name__line project-name__line--blue">LOS</span>
      <span class="project-name__line project-name__line--blue">PINOS</span>
      <span class="project-name__line project-name__line--dark">DE</span>
      <span class="project-name__line project-name__line--dark">ARENA</span>
    </h1>
    <div class="side-strip" role="img" aria-label="Narrow slice of the villa render showing sky and stone wall"></div>
  </div>
</body>
</html>
```